Dale Morven Broker owner of Real Estate Company

Dale Morven, HMP LRS ACX
Broker Owner
555-318-4627
dalemorven@dalemorvenrealtors.example
47362 Larchmont Ave. Lakeview Harbor, MI 48099
Licensed in Michigan and Florida
"37 Years of Outstanding Service based on a Result Driven Marketing Plan"

```html
<!DOCTYPE html>
<html lang="en">
<head>
<meta charset="utf-8">
<title>Dale Morven – Business Card</title>
<link href="https://fonts.googleapis.com/css2?family=Montserrat:wght@400;700&family=Cabin:wght@400&display=swap" rel="stylesheet">
<style>
  :root {
    --backdrop: #6e4630;
    --card-dark: #171717;
    --card-light: #ffffff;
    --gold: #eab86a;
    --ink: #333333;
    --rule: #555555;
    --photo-top: #5c625c;
    --photo-bottom: #2e3236;
  }
  * { margin: 0; padding: 0; box-sizing: border-box; }
  html, body { width: 1200px; height: 848px; overflow: hidden; }
  body { background: var(--backdrop); position: relative; font-family: "Montserrat", sans-serif; }

  .card { position: absolute; left: 261px; width: 655px; height: 356px; box-shadow: 0 6px 14px rgba(0,0,0,.35); }

  .card--front { top: 45px; background: var(--card-dark); text-align: center; }
  .front-name {
    position: absolute; left: 0; right: 0; top: 158px;
    font: 700 27px/1 "Montserrat", sans-serif; color: var(--gold); letter-spacing: .2px;
  }
  .front-tagline {
    position: absolute; left: 0; right: 0; top: 277px;
    font: 400 19px/24px "Cabin", sans-serif; color: #ffffff;
  }

  .card--back { top: 446px; background: var(--card-light); }
  .portrait {
    position: absolute; left: 33px; top: 32px; width: 116px; height: 139px;
    background: linear-gradient(180deg, var(--photo-top), var(--photo-bottom));
  }
  .identity { position: absolute; right: 32px; top: 190px; text-align: right; }
  .identity-name { font: 700 22px/1 "Montserrat", sans-serif; color: var(--gold); }
  .identity-name .credentials { font-size: 14px; }
  .identity-title { margin-top: 6px; font: 400 14.5px/1 "Montserrat", sans-serif; color: var(--ink); }
  .divider { position: absolute; left: 33px; right: 32px; top: 246px; border-top: 1px solid var(--rule); }

  .contact-list { position: absolute; left: 33px; top: 267px; list-style: none; }
  .contact-list li { display: flex; align-items: center; height: 20px; font: 400 14.5px/1 "Montserrat", sans-serif; color: var(--ink); }
  .icon { width: 13px; height: 13px; margin-right: 7px; flex: none; }
  .icon-solid { fill: var(--gold); stroke: none; }
  .icon-line { fill: none; stroke: var(--gold); stroke-width: 1.3; }
  .icon-cut { fill: none; stroke: #ffffff; stroke-width: 1.3; }

  .address { position: absolute; right: 32px; top: 288px; text-align: right; font: normal 400 14.5px/20.5px "Montserrat", sans-serif; color: var(--ink); }
</style>
</head>
<body>
  <section class="card card--front">
    <h1 class="front-name">Dale Morven, HMP LRS ACX</h1>
    <p class="front-tagline">37 Years of Outstanding Service based on a Result<br>Driven Marketing Plan</p>
  </section>

  <section class="card card--back">
    <div class="portrait" role="img" aria-label="Portrait photograph of Dale Morven"></div>
    <div class="identity">
      <h2 class="identity-name">Dale Morven, <span class="credentials">HMP LRS ACX</span></h2>
      <p class="identity-title">Broker Owner</p>
    </div>
    <div class="divider"></div>
    <ul class="contact-list">
      <li>
        <svg class="icon" viewBox="0 0 16 16" aria-hidden="true"><path class="icon-solid" d="M3.5 1l2.5 3-1.5 1.8c.8 1.8 2.2 3.2 4 4L10.3 8.3l3 2.5-1.3 2.7C7 13.5 2.5 9 2.5 3.5z"/></svg>
        555-318-4627
      </li>
      <li>
        <svg class="icon" viewBox="0 0 16 16" aria-hidden="true"><path class="icon-solid" d="M1 3h14v10H1z"/><path class="icon-cut" d="M1.5 3.5L8 9l6.5-5.5"/></svg>
        dalemorven@dalemorvenrealtors.example
      </li>
      <li>
        <svg class="icon" viewBox="0 0 16 16" aria-hidden="true"><g class="icon-line"><circle cx="8" cy="8" r="6.5"/><ellipse cx="8" cy="8" rx="2.8" ry="6.5"/><path d="M1.5 8h13M2.5 4.8h11M2.5 11.2h11"/></g></svg>
        www.dalemorvenrealtors.example
      </li>
    </ul>
    <address class="address">47362 Larchmont Ave.<br>Lakeview Harbor, MI 48099</address>
  </section>
</body>
</html>
```